Business Card Design

I want to pull elements/colors from Website. Attached is a screen shot. Do not want any buildings/building graphics/construction clichés. This is for a construction management firm but I want to keep it broad enough that I can expand into other areas. I do not want the logo to be limited. Thank you.
Updates

Please review the screen shot of the website. Please use the font and color of Brackwell Ventures, LLC on the website. Please use the tag line "Construction Management in the Palm Beaches" Please show contractor license ... CGC 4093615 You may use the back for the contact information. Please no phone/house icons. It does not have to be a black card. Thank you.

Target Market(s)

Professional people with money. Owners, Architects, Engineers, Developers, Real Estate Agents etc.

Industry/Entity Type

Construction

Contact Information for Business Card

Brackwell Ventures, LLC
Construction Management

Dale T Brackwell
240 Marlidge Court #14
North Palm Beach, FL 33408
(561) 555-0187
www.BrackwellVentures.example

Requirements
Must have
• Clean, crisp, modern.

Broad enough that it is not trapped into a particular industry.

My goal is to expand into different markets, different industries.

Should not have
• The back of the card should not be colored in any way. Rubs off on other cards.

Do not want any buildings/building graphics/construction clichés.

```html
<!DOCTYPE html>
<html lang="en">
<head>
<meta charset="utf-8">
<title>Brackwell Ventures — Business Card</title>
<link rel="stylesheet" href="https://fonts.googleapis.com/css2?family=Roboto+Condensed:wght@400;700&display=swap">
<style>
  :root {
    --page-bg: #e9e7e4;
    --card-light: #f2f2f2;
    --card-light-end: #d6d6d6;
    --band-dark: #2b2b2b;
    --band-mid: #4a4a4a;
    --frame-black: #1e1e1e;
    --ink-dark: #2a2a2a;
    --ink-grey: #8a8a8a;
    --rule: #3a3a3a;
    --white: #ffffff;
  }
  * { box-sizing: border-box; margin: 0; padding: 0; }
  html, body { width: 1200px; height: 900px; overflow: hidden; }
  body {
    background: var(--page-bg);
    font-family: "Roboto Condensed", "Arial Narrow", sans-serif;
    position: relative;
  }
  .card {
    position: absolute;
    width: 525px;
    height: 300px;
    box-shadow: 0 6px 18px rgba(0,0,0,0.18);
    overflow: hidden;
  }
  /* Front */
  .card-front {
    left: 50px; top: 300px;
    background: linear-gradient(180deg, var(--card-light) 0%, var(--card-light-end) 100%);
  }
  .front-band {
    position: absolute;
    left: 0; right: 0; top: 120px; height: 100px;
    background: linear-gradient(180deg, var(--band-mid) 0%, var(--band-dark) 100%);
    padding: 18px 0 0 32px;
    color: var(--white);
    font-weight: 700;
    line-height: 1.05;
  }
  .front-band .company { font-size: 30px; letter-spacing: 0.5px; }
  .front-band .division { font-size: 28px; }
  .front-tagline {
    position: absolute;
    left: 32px; top: 238px;
    font-size: 17px;
    font-weight: 700;
    color: var(--ink-dark);
  }
  /* Back */
  .card-back {
    left: 625px; top: 300px;
    background: var(--frame-black);
    padding: 14px;
  }
  .back-panel {
    position: relative;
    width: 100%; height: 100%;
    background: linear-gradient(180deg, var(--card-light) 0%, var(--card-light-end) 100%);
  }
  .back-name {
    position: absolute; right: 28px; top: 22px;
    font-size: 20px; font-weight: 700; letter-spacing: 0.5px;
    color: var(--ink-grey);
  }
  .rule { position: absolute; height: 1.5px; background: var(--rule); }
  .rule-top { left: 24px; right: 24px; top: 56px; }
  .rule-bottom { left: 24px; right: 24px; top: 170px; }
  .back-company {
    position: absolute; left: 24px; top: 110px;
    font-size: 27px; font-weight: 700; letter-spacing: 0.5px;
    color: var(--ink-dark);
  }
  .back-address {
    position: absolute; left: 24px; top: 144px;
    font-size: 14px; font-weight: 700; letter-spacing: 0.3px;
    color: var(--ink-dark);
  }
  .back-contact {
    position: absolute; left: 24px; top: 198px;
    font-size: 15px; font-weight: 700; line-height: 1.35;
    color: var(--ink-dark);
  }
  .back-license {
    position: absolute; right: 24px; top: 198px;
    font-size: 14px; font-weight: 700;
    color: var(--ink-dark);
  }
</style>
</head>
<body>
  <section class="card card-front" aria-label="Card front">
    <div class="front-band">
      <div class="company">BRACKWELL VENTURES</div>
      <div class="division">LLC Construction Management</div>
    </div>
    <p class="front-tagline">Construction Management in the Palm Beaches</p>
  </section>

  <section class="card card-back" aria-label="Card back">
    <div class="back-panel">
      <p class="back-name">DALE T BRACKWELL</p>
      <div class="rule rule-top"></div>
      <p class="back-company">BRACKWELL VENTURES</p>
      <p class="back-address">240 MARLIDGE COURT #14 NORTH PALM BEACH, FL 33408</p>
      <div class="rule rule-bottom"></div>
      <p class="back-contact">(561) 555-0187<br>www.BrackwellVentures.example</p>
      <p class="back-license">CGC 4093615</p>
    </div>
  </section>
</body>
</html>
```